New Website Design for Rides for Heroes.org - A Site for People to Donate Cars to War / Disabled Ve

Current site: www.ridesforheroes.org; Look at these sites for ideas: bikez2tots.org; gearsforhopes.org; www.autosformarines.org; www.trucksforsoldiers.org

Industry/Entity Type

Charity

Coding

Coded - Design and coding required

Number of Pages Required

1 page

Requirements
Must have
• n/a
Nice to have
• n/a
Should not have
• n/a

```html
<!DOCTYPE html>
<html lang="en">
<head>
<meta charset="utf-8">
<title>Rides for Heroes – Donate Your Car</title>
<link rel="stylesheet" href="https://fonts.googleapis.com/css2?family=Oswald:wght@300;400;500&family=Roboto:wght@300;400;500&display=swap">
<style>
:root{
  --blue:#2160b8;
  --blue-bright:#2f7de0;
  --red:#8e1b1b;
  --red-soft:#c0272d;
  --gold:#d4ad14;
  --gold-text:#f0d23a;
  --cream:#fcf9e6;
  --ink:#1c1c1c;
  --text:#333;
  --white:#fff;
  --backdrop-top:#8d9bbd;
  --backdrop-mid:#d6c3c8;
  --backdrop-low:#c98a92;
}
*{box-sizing:border-box;margin:0;padding:0}
html,body{width:1200px;height:1200px;overflow:hidden}
body{font-family:"Roboto",sans-serif;color:var(--text);position:relative}
.page-backdrop{position:absolute;inset:0;
  background:linear-gradient(180deg,var(--backdrop-top) 0%,var(--backdrop-mid) 45%,var(--backdrop-low) 75%,var(--backdrop-mid) 100%)}
.sheet{position:absolute;left:150px;top:0;width:900px;height:1200px;background:rgba(238,238,242,.7)}
.wrap{position:absolute;left:164px;width:874px}

.site-header{top:18px;height:78px;background:var(--blue);display:flex;align-items:center;justify-content:space-between;padding:0 14px 0 30px}
.brand{font-weight:400;font-size:20px;color:var(--white);display:flex;align-items:center;gap:10px}
.brand-mark{width:14px;height:14px;background:var(--red-soft);border-radius:50%}
.header-contact{display:flex;align-items:center;gap:11px}
.help{text-align:right;color:var(--white)}
.help .lead{font-weight:300;font-size:21px}
.help .sub{font-size:11px;margin-top:4px}
.help .sub b{color:var(--gold-text);font-weight:500}
.phone-box{background:var(--blue-bright);height:51px;width:203px;display:flex;align-items:center;justify-content:center;gap:12px;color:var(--white);font-family:"Oswald",sans-serif;font-size:19px}

.hero{top:100px;height:282px;background:linear-gradient(90deg,#2d2f3a 0%,#6b5a4a 30%,#a08a5a 50%,#3f6d7c 70%,#9c8044 100%)}

.features{top:382px;height:59px;display:flex}
.feature{flex:1;display:flex;align-items:center;justify-content:center;gap:12px;color:var(--white);font-family:"Oswald",sans-serif;font-size:15px;line-height:19px}
.feature.black{background:#0a0a0a}.feature.red{background:var(--red)}
.feature.blue{background:var(--blue)}.feature.gold{background:var(--gold)}

.why{top:454px;height:364px;background:var(--cream);padding:22px 24px 0 24px}
.why h2{font-weight:400;font-size:20px;color:var(--blue);padding-bottom:12px;border-bottom:1px solid #888}
.why-cols{display:flex;gap:56px;margin-top:23px}
.why-col{flex:1}
.why-col:first-child{flex:0 0 380px}
.point{position:relative;padding-left:24px;margin-bottom:12px}
.point::before{content:"›";position:absolute;left:0;top:2px;width:15px;height:15px;border-radius:50%;background:var(--red-soft);color:#fff;font-size:13px;line-height:13px;text-align:center}
.point h3{font-family:"Oswald",sans-serif;font-weight:500;font-size:14px;color:var(--ink);margin-bottom:2px}
.point p{font-size:11.6px;line-height:20px;color:#222}

.donate-form{top:830px;height:207px;background:linear-gradient(135deg,#1b3f90 0%,#2763c2 40%,#1c4aa3 70%,#2a68c8 100%);padding:24px 22px 0 22px;color:var(--white)}
.donate-form h2{font-family:"Oswald",sans-serif;font-weight:400;font-size:19px}
.donate-form .note{font-size:12px;margin:2px 0 17px 2px}
.fields{display:grid;grid-template-columns:repeat(3,1fr);gap:6px 4px}
.field{height:28px;border:1px solid #8fb0e8;padding-left:12px;font-size:11px;line-height:26px;color:var(--white);position:relative}
.field.select::after{content:"";position:absolute;right:10px;top:10px;border:5px solid transparent;border-top:8px solid #fff;border-bottom:0}
.submit{height:28px;background:var(--gold);color:#1a1a1a;font-size:11.5px;text-align:center;line-height:28px}

.site-footer{top:1050px;height:127px;background:#fafafa;border:1px solid #ccc;padding:16px 22px}
.site-footer h2{font-family:"Oswald",sans-serif;font-weight:400;font-size:22px;color:var(--red)}
.site-footer .strong{font-weight:500;font-size:12.5px;color:#111;margin:4px 0 11px}
.ticks{display:grid;grid-template-columns:190px 230px;gap:7px 0;font-size:11px;color:#333}
.ticks li{list-style:none;padding-left:14px;position:relative}
.ticks li::before{content:"";position:absolute;left:2px;top:4px;width:5px;height:5px;background:#222}
.badges{position:absolute;right:14px;top:33px;display:flex;gap:30px;align-items:center}
.badge-plate{width:136px;height:44px;background:#0f3f72}
.badge-seal{width:48px;height:48px;border-radius:50%;background:#4d8fc7}
.badge-secure{width:98px;height:32px;background:#c8202a;border-radius:4px}
.copyright{position:absolute;right:14px;bottom:22px;font-size:11px;color:#333}
</style>
</head>
<body>
<div class="page-backdrop" role="img" aria-label="Photo of a waving American flag behind the page"></div>
<div class="sheet"></div>

<header class="wrap site-header">
  <div class="brand"><span class="brand-mark"></span>Rides for Heroes</div>
  <div class="header-contact">
    <div class="help"><div class="lead">We need your help</div><div class="sub">Live Operators Available <b>7 Days A Week</b></div></div>
    <div class="phone-box">
      <svg width="26" height="22" viewBox="0 0 26 22" fill="#fff"><path d="M2 8c0-4 4-6 11-6s11 2 11 6v2h-6V7H8v3H2z"/><rect x="5" y="11" width="16" height="10" rx="2"/></svg>
      <span>1 - 800 - 555 - 0142</span>
    </div>
  </div>
</header>

<div class="wrap hero" role="img" aria-label="Veterans marching with flags beside a classic blue car in tall grass"></div>

<section class="wrap features">
  <div class="feature black"><svg width="30" height="30"><circle cx="15" cy="15" r="12" fill="#fff"/></svg><span>Donations accepted<br>nationwide</span></div>
  <div class="feature red"><svg width="46" height="32" viewBox="0 0 46 32" fill="#fff"><rect x="2" y="4" width="26" height="20"/><path d="M30 10h8l6 8v6H30z"/><circle cx="10" cy="27" r="4"/><circle cx="36" cy="27" r="4"/></svg><span>All vehicle types<br>welcome</span></div>
  <div class="feature blue"><svg width="34" height="36" viewBox="0 0 34 36" fill="none" stroke="#fff" stroke-width="2.5"><rect x="3" y="5" width="22" height="28"/><path d="M8 14h12M8 20h12M8 26h8M20 28l12-20"/></svg><span>Tax deductible</span></div>
  <div class="feature gold"><svg width="54" height="32" viewBox="0 0 54 32" fill="#fff"><path d="M2 14h16l4-8h10v16H2z"/><path d="M32 20l18-16 2 2-16 16z"/><circle cx="10" cy="25" r="5"/><circle cx="28" cy="25" r="5"/></svg><span>Towing is free</span></div>
</section>

<section class="wrap why">
  <h2>Why Donate Your Car to Us?</h2>
  <div class="why-cols">
    <div class="why-col">
      <div class="point"><h3>BTC A+ Rated &amp; IRS 501(c)3 Approved:</h3><p>Free 24/7 Pickup with No DMV Hassles..</p></div>
      <div class="point"><h3>Free Local Towing:</h3><p>We will pick up your car donation, running or not, when it's most convenient, at home or work.</p></div>
      <div class="point"><h3>All Cars Accepted:</h3><p>We take your car regardless of its condition or registration status.</p></div>
      <div class="point"><h3>Income Tax Deduction:</h3><p>We issue you an IRS tax receipt &amp; offer the largest resale network to get you the highest tax write-off possible.</p></div>
    </div>
    <div class="why-col">
      <div class="point"><h3>No Paperwork Hassles:</h3><p>We take any car and handle everything: DMV, Smog and IRS paperwork.</p></div>
      <div class="point"><h3>Car donations help fund programs:</h3><p>And benefit National Heroes Support Fund. An IRS 501(c)3 nonprofit organization.</p></div>
      <div class="point"><h3>Schedule a Free Pickup:</h3><p>Complete the form and a representative will call you to arrange a convenient time to pickup your car.</p></div>
    </div>
  </div>
</section>

<section class="wrap donate-form">
  <h2>Donate Your Car: Full Tax Deduction - Running or Not</h2>
  <p class="note">Please fill out form or Call toll-free 1-800-555-0142</p>
  <div class="fields">
    <div class="field">Name:</div><div class="field">Phone No:</div><div class="field">Address:</div>
    <div class="field select">-Select-</div><div class="field">Email:</div><div class="field">Cell Phone:</div>
    <div class="field">City:</div><div class="field">Zip Code:</div><div class="submit">Click Here To Donate Now</div>
  </div>
</section>

<footer class="wrap site-footer">
  <h2>Donate Your Car Today!</h2>
  <p class="strong">You have no costs.</p>
  <ul class="ticks">
    <li>Free towing, running or not.</li><li>We take care of all paperwork.</li>
    <li>We issue you an IRS tax receipt.</li><li>And we take care of DMV &amp; Smog issues.</li>
  </ul>
  <div class="badges"><div class="badge-plate"></div><div class="badge-seal"></div><div class="badge-secure"></div></div>
  <p class="copyright">Copyright © 2016 &nbsp;Rides for Heroes . All rights reserved</p>
</footer>
</body>
</html>
```